Webdesign for Dutch IT consultancy company

Make a Wordpress webdesign for a Dutch consultancy company

Briefing Velmora IT

Website for finding and connecting IT-professionals. Corebusiness is to find IT-professionals and to help them to follow their ambitions. We offer training, personal coaching and education trajects.

U can take www.Tralvique.nl as an example for the website.

Home page

U can take www.Tralvique.nl as an example.

There should be jobs on the home page. A block for short info about us and about what whe do and a trigger to contact us quickly.

Jobs Page

On this page should be the jobs that we offer for the professionals. There should be a search function on this page so u can easily find the job that you are looking for.

A call to action can be on this page too.

Also a little block with text for some information.

For professionals page

Block with information on top. Call to action. info about who we work for/with.

For Clients

Info about three different solutions

- Sourcing solutions
- Consultancy solutions
- Custom based traineeships

Request a qoute option

Traineeships page

Info about two different traineeships

- Linux traineeships
- Microsoft traineeships

Call to action/ subscribe for traineeships

About us page

We are Velmora IT

Our mission: Creating cooperations between young professionals and businesses who wanna work on a great future.

Our core values

Last news

Target Market(s)

Young professionals and businesses who need IT services

Industry/Entity Type

It Company

Coding

Coded - Design and coding required

Number of Pages Required

5+ page

Font styles to use
Other font styles liked:
• Calibri

Colors
ffffff
add136
6b449b

Requirements
Must have
• Home page, Jobs Page, Professionals page, Clients page, Traineeships page, About us Page
• Green and/or Purple layout. Job search option, subscribe option
Nice to have
• modern design

```html
<!DOCTYPE html>
<html lang="en">
<head>
<meta charset="utf-8">
<title>Velmora IT – Home</title>
<link href="https://fonts.googleapis.com/css2?family=Open+Sans:wght@400;600;700;800&display=swap" rel="stylesheet">
<style>
:root{
  --purple:#6b449b;
  --purple-deep:#3c1f4d;
  --purple-dark:#2e1a3a;
  --green:#add136;
  --ink:#2b2b2b;
  --muted:#8a8a8a;
  --line:#e4e4e4;
  --footer:#2b2229;
  --footer-bar:#1d171c;
  --white:#ffffff;
}
*{box-sizing:border-box;margin:0;padding:0}
html,body{width:1200px;height:3197px;overflow:hidden}
body{font-family:"Open Sans",Arial,sans-serif;color:var(--ink);background:var(--white);position:relative;font-size:13px}
.abs{position:absolute}
a{color:inherit;text-decoration:none}

/* header */
.site-header{position:absolute;top:0;left:0;width:1200px;height:93px;background:var(--white);border-bottom:1px solid var(--line)}
.brand{position:absolute;left:172px;top:30px;font-weight:800;font-size:30px;color:var(--purple);letter-spacing:.5px}
.brand small{display:block;font-size:8px;font-weight:600;color:var(--green);letter-spacing:2px;margin-top:-4px}
.main-nav{position:absolute;left:416px;top:42px;display:flex;gap:26px;font-size:13px;color:#555}
.main-nav .active{color:var(--purple);font-weight:600}
.main-nav .caret::after{content:" ▾";font-size:9px}

/* hero */
.hero{position:absolute;top:93px;left:0;width:1200px;height:436px;background:linear-gradient(180deg,#cfe3d5 0%,#9fc39a 45%,#6f9a53 100%)}
.hero-box{position:absolute;left:687px;top:228px;width:340px;height:180px;background:rgba(52,22,62,.88);padding:24px 18px}
.hero-box h1{color:var(--white);font-size:20px;font-weight:700;line-height:1.55;text-transform:uppercase}
.hero-btns{margin-top:18px;display:flex;gap:8px}
.btn-sm{font-size:11px;padding:7px 12px;text-transform:uppercase;font-weight:600}
.btn-light{background:#eee;color:#333}
.btn-purple{background:var(--purple);color:var(--white)}

/* jobs */
.section-title{font-size:20px;font-weight:700;color:var(--ink)}
.jobs-title{left:172px;top:570px}
.job-list{position:absolute;left:162px;top:618px;width:571px;border-top:2px solid #bbb}
.job{position:relative;height:118px;border-bottom:1px solid var(--line)}
.job:nth-child(1){background:#fdfdf6}
.job:nth-child(2){background:#eff8ee;margin-top:10px}
.job:nth-child(3){background:#fff;margin-top:10px}
.job:nth-child(4){background:#f6f6f6;margin-top:10px}
.job-logo{position:absolute;left:18px;top:34px;width:50px;height:50px;border:1px solid var(--line);background:var(--white);display:flex;align-items:center;justify-content:center;font-size:10px;font-weight:700;color:var(--purple);text-align:center;line-height:1.1}
.job h3{position:absolute;left:86px;top:34px;font-size:15px;font-weight:600}
.job-meta{position:absolute;left:86px;top:66px;font-size:11px;color:#666;display:flex;gap:16px}
.job-meta span::before{content:"";display:inline-block;width:8px;height:8px;background:#999;margin-right:5px;border-radius:1px}
.job-meta .pin::before{border-radius:50% 50% 50% 0}
.btn-more{position:absolute;left:340px;top:1156px;width:228px;height:40px;background:var(--purple-deep);color:var(--white);font-size:12px;font-weight:700;display:flex;align-items:center;justify-content:center;text-transform:uppercase;gap:8px}
.btn-more i{width:14px;height:14px;border-radius:50%;background:var(--white);display:inline-block}

.spot-title{left:760px;top:570px}
.spot-arrows{position:absolute;left:997px;top:574px;font-size:16px;color:#555;letter-spacing:6px}
.card{position:absolute;background:#f4f4f4;border:1px solid var(--line)}
.spotlight{left:757px;top:615px;width:271px;height:330px;padding:26px 18px}
.spotlight h3{font-size:14px;font-weight:600;color:#444;line-height:1.4}
.spot-line{font-size:11px;color:#666;margin-top:10px;padding-left:18px;position:relative;line-height:1.4}
.spot-line::before{content:"";position:absolute;left:0;top:3px;width:8px;height:8px;background:#999}
.spotlight p{font-size:11px;color:#666;line-height:1.5;margin-top:16px}
.btn-block{display:block;margin:18px auto 0;width:180px;height:34px;background:var(--purple-deep);color:var(--white);font-size:11px;font-weight:700;text-transform:uppercase;display:flex;align-items:center;justify-content:center}
.upload{left:757px;top:964px;width:271px;height:178px;padding:22px 18px;text-align:center}
.upload h3{font-size:15px;font-weight:600}
.upload p{font-size:10px;color:#777;line-height:1.5;margin-top:8px}

/* about + quote */
.about{position:absolute;top:1237px;left:0;width:593px;height:435px;background:linear-gradient(135deg,#4a2f5c,#2f1c3c)}
.about-inner{position:absolute;left:187px;top:50px;width:330px;color:var(--white)}
.about h2{font-size:21px;font-weight:700}
.rule{width:36px;height:2px;background:var(--white);margin:10px 0 34px}
.about p{font-size:12px;line-height:1.6;margin-bottom:16px}
.btn-white{display:inline-block;background:var(--white);color:#333;font-size:10px;font-weight:700;padding:8px 12px;text-transform:uppercase}
.quote{position:absolute;top:1237px;left:593px;width:607px;height:435px;background:var(--purple)}
.quote-inner{position:absolute;left:37px;top:50px;width:390px;color:var(--white)}
.quote h2{font-size:21px;font-weight:700}
.quote .sub{font-size:11px;margin-top:8px}
.form-grid{display:grid;grid-template-columns:1fr 1fr;gap:15px 27px;margin-top:45px}
.field{height:34px;background:var(--white);color:#999;font-size:11px;padding:9px 10px}
.field.msg{grid-column:1/3;height:86px}
.btn-submit{display:inline-block;margin-top:20px;background:var(--white);color:#333;font-size:12px;font-weight:700;padding:10px 30px;text-transform:uppercase}

/* services */
.services{position:absolute;top:1672px;left:0;width:1200px;height:546px;background:#f2f2f2}
.center-title{position:absolute;left:0;width:1200px;text-align:center}
.services .t{top:56px;font-size:20px;font-weight:700}
.services .s{top:100px;font-size:13px;color:#666}
.service{position:absolute;width:209px;height:123px;background:var(--white);box-shadow:0 2px 6px rgba(0,0,0,.08);text-align:center;padding:40px 16px 0}
.service h4{font-size:14px;font-weight:600;text-transform:uppercase;color:#333}
.service p{font-size:10px;color:#888;line-height:1.5;margin-top:8px}
.service .ico{position:absolute;left:50%;top:-32px;margin-left:-30px;width:60px;height:60px;border-radius:50%;background:var(--white);border:2px solid #d9cbe8;display:flex;align-items:center;justify-content:center}
.people{position:absolute;left:406px;top:189px;width:393px;height:357px;background:linear-gradient(180deg,#e9e6ea,#3b3a42)}

/* newsletter */
.newsletter{position:absolute;top:2218px;left:0;width:1200px;height:221px;background:linear-gradient(90deg,var(--purple-dark),#3f2250 50%,var(--purple-dark))}
.newsletter .t{top:44px;color:var(--white);font-size:20px;font-weight:700}
.newsletter .s{top:92px;color:var(--white);font-size:13px}
.news-form{position:absolute;left:359px;top:138px;width:482px;height:40px;display:flex}
.news-form .input{flex:1;background:var(--white);font-size:12px;color:#999;padding:11px 14px}
.news-form .go{width:54px;background:var(--purple);display:flex;align-items:center;justify-content:center}

/* news */
.latest{position:absolute;top:2439px;left:0;width:1200px;height:458px;background:var(--white)}
.latest .t{top:52px;font-size:20px;font-weight:700;text-transform:uppercase}
.latest .s{top:100px;font-size:13px;color:#666}
.post{position:absolute;top:160px;width:271px}
.post .img{height:108px;background:linear-gradient(135deg,#b9c7d6,#6e7f92)}
.post .avatar{position:absolute;left:20px;top:90px;width:34px;height:34px;border-radius:50%;background:#c9c9c9;border:2px solid var(--white)}
.post h4{font-size:14px;font-weight:600;line-height:1.4;margin-top:26px}
.post .meta{font-size:10px;color:#999;margin-top:6px;display:flex;gap:14px}
.post p{font-size:11px;color:#777;line-height:1.5;margin-top:8px}

/* footer */
.site-footer{position:absolute;top:2897px;left:0;width:1200px;height:260px;background:var(--footer);color:#ddd}
.fcol{position:absolute;top:40px}
.fcol h5{font-size:14px;font-weight:700;color:var(--white);text-transform:uppercase}
.fcol .rule{width:28px;height:2px;background:var(--white);margin:8px 0 20px}
.contact-line{font-size:12px;line-height:1.45;margin-bottom:14px;display:flex;gap:14px;width:220px}
.social{display:flex;gap:14px;margin-left:22px}
.social i{width:10px;height:10px;background:#ddd;display:block}
.links{display:grid;grid-template-columns:115px 120px;row-gap:6px;font-size:12px}
.btn-quote{display:inline-block;margin-top:18px;background:var(--purple);color:var(--white);font-size:12px;font-weight:700;padding:9px 20px;text-transform:uppercase}
.map{position:absolute;left:767px;top:86px;width:249px;height:165px;background:linear-gradient(135deg,#e8eddf,#c7d7e6)}
.to-top{position:absolute;left:1088px;top:196px;width:30px;height:30px;background:var(--purple);transform:rotate(45deg)}
.bottom-bar{position:absolute;top:3157px;left:0;width:1200px;height:40px;background:var(--footer-bar);color:#bbb;font-size:11px;padding:13px 172px}
</style>
</head>
<body>

<header class="site-header">
  <div class="brand">Velmora IT<small>IT PROFESSIONALS</small></div>
  <nav class="main-nav">
    <a class="active">Home</a><a class="caret">Jobs</a><a class="caret">For Professionals</a><a class="caret">For Clients</a><a class="caret">Traineeships</a><a class="caret">About Us</a><a>Contact Us</a>
  </nav>
</header>

<section class="hero" role="img" aria-label="Two young professionals sitting on a lawn working on a laptop">
  <div class="hero-box">
    <h1>We are here to help you to follow your ambition</h1>
    <div class="hero-btns"><span class="btn-sm btn-light">IT Vacancies</span><span class="btn-sm btn-purple">Request a Quote</span></div>
  </div>
</section>

<h2 class="abs section-title jobs-title">Recent It Jobs</h2>
<div class="job-list">
  <div class="job"><div class="job-logo">Linkwise Info</div><h3>Network Engineer</h3>
    <div class="job-meta"><span>Linkwise Info</span><span class="pin">115,Cillum dolore eu fugiat nulla pariatur</span><span>$40000 - $50000</span></div></div>
  <div class="job"><div class="job-logo">Datora</div><h3>Software Developer</h3>
    <div class="job-meta"><span>Datora</span><span class="pin">115,Aut reiciendis voluptatibus maiores</span><span>$30000 - $60000</span></div></div>
  <div class="job"><div class="job-logo">Helix Aero</div><h3>Project Manager</h3>
    <div class="job-meta"><span>Helix Aero</span><span class="pin">115,Cumque nihil impedit quo minus</span><span>$35000 - $50000</span></div></div>
  <div class="job"><div class="job-logo">Orvin Smith</div><h3>Computer and Information Expert</h3>
    <div class="job-meta"><span>Orvin Smith</span><span class="pin">115,Reiciendis voluptatibus maiores</span><span>$40000 - $50000</span></div></div>
</div>
<a class="btn-more"><i></i>View more jobs</a>

<h2 class="abs section-title spot-title">Job Spotlight</h2>
<div class="spot-arrows">‹ ›</div>
<div class="card spotlight">
  <h3>Senior Onsite Support Engineer</h3>
  <div class="spot-line">Norvel Industrial</div>
  <div class="spot-line">55A/3,Cum soluta nobis est eligendi optio cumque</div>
  <div class="spot-line">$30000 - $35000</div>
  <p>Nostrum exercitationem ullam corporis suscipit laboriosam, nisi ut aliquid ex ea commodi in ea voluptate velit esse quam nihil molestiae</p>
  <a class="btn-block">Apply for this job</a>
</div>
<div class="card upload">
  <h3>Upload Your Resume</h3>
  <p>Nemo enim ipsam voluptatem quia voluptas sit aspernatur aut odit aut fugit, sed quia consequuntur magni dolores eos qui</p>
  <a class="btn-block" style="width:150px">Upload Resume</a>
</div>

<section class="about">
  <div class="about-inner">
    <h2>About Velmora IT</h2><div class="rule"></div>
    <p>Corebusiness is to find IT-professionals and to help them to follow their ambitions.</p>
    <p>Our mission is to Creating cooperations between young professionals and businesses who wanna work on a great future.</p>
    <span class="btn-white">Contact Us</span>
  </div>
</section>
<section class="quote">
  <div class="quote-inner">
    <h2>Request a Quote</h2>
    <div class="sub">Numquam eius modi tempora incidunt</div>
    <div class="form-grid">
      <div class="field">First Name *</div><div class="field">Last Name *</div>
      <div class="field">Email...</div><div class="field">Phone No...</div>
      <div class="field msg">Message...</div>
    </div>
    <span class="btn-submit">Submit</span>
  </div>
</section>

<section class="services">
  <h2 class="center-title t">Our Services</h2>
  <p class="center-title s">Reprehenderit qui in ea voluptate velit esse quam nihil molestiae</p>
  <div class="service" style="left:172px;top:192px"><div class="ico"><svg width="26" height="26" viewBox="0 0 26 26" fill="none" stroke="#6b449b" stroke-width="2"><rect x="4" y="4" width="18" height="13"/><path d="M13 17v6M8 23h10"/></svg></div><h4>Training</h4><p>Neque porro quisquam est qui dolorem ipsum quia dolor</p></div>
  <div class="service" style="left:172px;top:364px"><div class="ico"><svg width="26" height="26" viewBox="0 0 26 26" fill="none" stroke="#6b449b" stroke-width="2"><rect x="5" y="3" width="16" height="20"/><path d="M9 9h8M9 13h8M9 17h5"/></svg></div><h4>Education Projects</h4><p>Quis nostrud exercitation ullamco laboris nisi ut ea commodo</p></div>
  <div class="service" style="left:819px;top:192px"><div class="ico"><svg width="26" height="26" viewBox="0 0 26 26" fill="none" stroke="#6b449b" stroke-width="2"><circle cx="13" cy="9" r="5"/><path d="M4 24c0-6 4-9 9-9s9 3 9 9"/></svg></div><h4>Personal Coaching</h4><p>Ipsum voluptatem quia voluptas sit aspernatur aut odit aut</p></div>
  <div class="service" style="left:819px;top:364px"><div class="ico"><svg width="26" height="26" viewBox="0 0 26 26" fill="none" stroke="#6b449b" stroke-width="2"><circle cx="11" cy="11" r="7"/><path d="M16 16l7 7"/></svg></div><h4>Find IT Professionals</h4><p>Voluptate velit esse cillum dolore eu fugiat nulla pariatur</p></div>
  <div class="people" role="img" aria-label="Two smiling business professionals standing back to back"></div>
</section>

<section class="newsletter">
  <h2 class="center-title t">Newsletter</h2>
  <p class="center-title s">Subscribe to our Newsletter for Traineeships</p>
  <div class="news-form"><div class="input">Email...</div><div class="go"><svg width="16" height="16" viewBox="0 0 16 16"><path d="M1 8l14-6-5 13-2-5z" fill="#fff"/></svg></div></div>
</section>

<section class="latest">
  <h2 class="center-title t">Latest News</h2>
  <p class="center-title s">Temporibus autem quibusdam et aut officiis debitis aut rerum necessitatibus</p>
  <article class="post" style="left:172px"><div class="img" role="img" aria-label="Group of students outdoors"></div><div class="avatar"></div>
    <h4>Reiciendis voluptatibus maiores alias consequatur aut</h4><div class="meta"><span>Lars Vermeer</span><span>18th Nov 2017</span></div>
    <p>Officiis debitis aut rerum necessitatibus saepe eveniet ut et voluptates sint et molestiae non recusandae maiores alias consequatur</p></article>
  <article class="post" style="left:465px"><div class="img" role="img" aria-label="Technician working at a server rack"></div><div class="avatar"></div>
    <h4>Reiciendis voluptatibus maiores alias consequatur aut</h4><div class="meta"><span>Pim Dekker</span><span>18th Nov 2017</span></div>
    <p>Officiis debitis aut rerum necessitatibus saepe eveniet ut et voluptates sint et molestiae non recusandae maiores alias consequatur</p></article>
  <article class="post" style="left:757px"><div class="img" role="img" aria-label="Professional working at a desk with a laptop"></div><div class="avatar"></div>
    <h4>Reiciendis voluptatibus maiores alias consequatur aut</h4><div class="meta"><span>Sem Koster</span><span>18th Nov 2017</span></div>
    <p>Officiis debitis aut rerum necessitatibus saepe eveniet ut et voluptates sint et molestiae non recusandae maiores alias consequatur</p></article>
</section>

<footer class="site-footer">
  <div class="fcol" style="left:182px">
    <h5>Contact Us</h5><div class="rule"></div>
    <div class="contact-line"><span>⌖</span><span>12/1, reiciendis voluptatibus maiores alias consequatur</span></div>
    <div class="contact-line"><span>✆</span><span>0880 200 300</span></div>
    <div class="contact-line"><span>✉</span><span>info@velmorait.nl</span></div>
    <div class="social"><i></i><i></i><i></i><i></i></div>
  </div>
  <div class="fcol" style="left:467px">
    <h5>Useful Links</h5><div class="rule"></div>
    <div class="links"><span>About Us</span><span>For Clients</span><span>Traineeships</span><span>Custom based traineeships</span><span>For Professionals</span><span>News</span><span>Contact Us</span><span>Privacy Policy</span></div>
    <span class="btn-quote">Request a Quote</span>
  </div>
  <div class="fcol" style="left:760px"><h5>Locate Us</h5><div class="rule"></div></div>
  <div class="map" role="img" aria-label="Map showing the office location in Amsterdam"></div>
  <div class="to-top"></div>
</footer>
<div class="bottom-bar">©Copyright information here</div>

</body>
</html>
```